Package & Pricing Guide

We need a package and pricing brochure for our premium wedding cinematography company. Brochure should reflect company branding and colors, as found here: www.valmorafilmworks.com.

Brochure should be Bi-fold, WIDTH: outside pages 11"/Inside pages 5.5" HEIGHT: 8.5". All logos, images, and wording can be provided if necessary. Must be able to provide the original PSD template, fonts used and assets so that we can customize to fit the different pricing variances throughout the year.

We have two separate groups of packages, each should take up a "2 sheet spread". Left hand page for description, right hand page for pricing and package information. Design should also include area for some images, places to talk about our company, additional or add-on services, and awards. Contact info placeholders as well.

We are attaching our logo in PSD, and our current package guide for reference, feel free to use the text if needed. When text is not available, "lorem Ipsum" is acceptable.

Target Market(s)

Engaged, young couples seeking a premium service.

Industry/Entity Type

Wedding

Requirements
Must have
• PSD template
All assets
Company Logo
"About us" section
2 page spread per package (3 total packages)
Placeholders for images that we can provide

```html
<!DOCTYPE html>
<html lang="en">
<head>
<meta charset="utf-8">
<title>Valmora Filmworks – Package &amp; Pricing Guide</title>
<link href="https://fonts.googleapis.com/css2?family=Jost:wght@400;500;600&family=Barlow+Semi+Condensed:wght@500;600;700&display=swap" rel="stylesheet">
<style>
:root{
  --blue:#1f6fc0;
  --blue-dark:#17589c;
  --ink:#2b2b2d;
  --muted:#4a4a4d;
  --night:#1c1c1e;
  --paper-a:#ffffff;
  --paper-b:#e3e4e6;
  --backdrop:#d9d6d2;
}
*{box-sizing:border-box;margin:0;padding:0}
html,body{width:1200px;height:2671px;overflow:hidden;background:var(--backdrop)}
body{position:relative;font-family:"Jost",sans-serif;color:var(--ink)}
.page{position:absolute;width:509px;height:787px;background:linear-gradient(90deg,var(--paper-a) 55%,var(--paper-b));overflow:hidden;box-shadow:0 2px 8px rgba(0,0,0,.18)}
.page::after{content:"";position:absolute;left:0;right:0;bottom:0;height:12px;background:var(--blue)}
.p1{left:57px;top:53px}.p2{left:634px;top:53px}
.p3{left:57px;top:899px}.p4{left:634px;top:992px}
.p5{left:57px;top:1741px}.p6{left:634px;top:1842px}
.photo{position:absolute}
.inner{padding:30px 40px 0 44px}
.heading{font-family:"Barlow Semi Condensed",sans-serif;font-weight:600;color:var(--blue);font-size:23px;letter-spacing:.3px;display:flex;align-items:center;gap:9px;margin-bottom:12px}
.heading .mark{width:9px;height:9px;background:var(--night);flex:none}
.body{font-size:8.6px;line-height:1.38;color:var(--muted)}
.body p{margin-bottom:7px}
.lead-in{font-style:italic;margin:6px 0 4px 14px}
.dots{list-style:none;margin-left:22px}
.dots li{position:relative;padding-left:13px;margin-bottom:7px}
.dots li::before{content:"";position:absolute;left:0;top:3px;width:6px;height:6px;border-radius:50%;background:var(--blue)}
.dots .note{display:block;font-style:italic;margin-left:8px}
.price-box{background:var(--blue);color:#fff;font-weight:600;font-size:11.5px;line-height:1.4;padding:5px 12px;margin:10px 0 8px 4px}
.label{display:inline-block;background:var(--blue);color:#fff;font-weight:500;font-size:10.5px;padding:4px 14px;margin:6px 0 5px}
.label.wide{width:260px}
.label.slim{font-size:8.6px;font-style:italic;padding:3px 10px;width:225px}
.ticks{list-style:none;margin-left:2px}
.ticks li{display:flex;align-items:center;gap:7px;margin-bottom:3.5px}
.ticks svg{flex:none}
.grid{position:absolute;left:0;right:0;display:grid;grid-template-columns:1fr 1fr;gap:8px}
.grid .photo{position:static;height:100%}
/* page 1 */
.p1 .hero{left:0;top:0;width:509px;height:535px;background:linear-gradient(180deg,#6d9fd4 0%,#b8d3ea 42%,#7aa2bd 52%,#b59a77 64%,#8a6d4e 100%)}
.p1 .dark{position:absolute;left:0;top:535px;width:509px;height:240px;background:var(--night);color:#fff}
.tagline{text-align:center;font-size:12.5px;line-height:1.4;padding:14px 50px 0}
.quality{position:absolute;left:30px;top:92px;width:200px}
.quality h3{font-family:"Barlow Semi Condensed",sans-serif;font-weight:600;color:var(--blue);font-size:19px;margin-bottom:4px}
.quality p{font-size:8.6px;line-height:1.35;color:#e8e8e8}
.brand{position:absolute;font-family:"Jost",sans-serif;font-weight:400;color:#fff;text-align:center;letter-spacing:6px}
.p1 .brand{left:270px;top:120px;width:200px;font-size:30px;line-height:1.1}
.brand small{display:block;font-size:10px;letter-spacing:4px;margin-top:6px}
/* page 6 */
.p6 .top{position:absolute;left:0;top:0;width:509px;height:515px;background:var(--blue)}
.p6 .venues{position:absolute;left:0;top:55px;width:509px;height:115px;display:grid;grid-template-columns:1fr 1fr;gap:4px;background:#dfe6ee}
.p6 .venues .photo{position:static}
.p6 .band{position:absolute;left:0;top:170px;width:509px;height:10px;background:linear-gradient(90deg,#c9ccd0,#fff,#c9ccd0)}
.about{position:absolute;left:40px;right:40px;top:196px;color:#fff;font-size:8.4px;line-height:1.38}
.about h2{font-family:"Barlow Semi Condensed",sans-serif;font-weight:600;text-align:center;font-size:22px;margin-bottom:8px}
.about p{margin-bottom:7px}
.about .loc{font-weight:600}
.p6 .bottom{position:absolute;left:0;top:515px;width:509px;height:260px;background:var(--night);color:#fff}
.p6 .band2{position:absolute;left:0;top:515px;width:509px;height:8px;background:linear-gradient(90deg,#9ea2a8,#fff,#9ea2a8)}
.award{text-align:center;font-family:"Barlow Semi Condensed",sans-serif;font-weight:600;color:var(--blue);font-size:20px;letter-spacing:.5px;margin-top:24px}
.badges{position:absolute;left:0;right:0;top:68px;display:flex;justify-content:center;gap:34px}
.p6 .brand{left:55px;top:186px;width:150px;font-size:26px;line-height:1}
.p6 .brand small{font-size:8px;letter-spacing:3px}
.contact{position:absolute;left:250px;top:184px;list-style:none;font-size:10px;line-height:1.6}
.contact li{display:flex;align-items:center;gap:6px}
.contact .phone{font-weight:600;font-size:11.5px}
/* FAQ */
.faq h4{font-weight:500;color:var(--blue);font-size:11.2px;line-height:1.25;margin:7px 0 3px}
.faq p{font-size:8.4px;line-height:1.36;color:var(--muted)}
</style>
</head>
<body>

<section class="page p1">
  <div class="photo hero" role="img" aria-label="Bride and groom embracing on a sandy beach under a blue sky"></div>
  <div class="dark">
    <p class="tagline">We are a boutique cinematography studio dedicated to creating inspiring films that capture your story. Take a look around our portfolio, we hope that you love what you see!</p>
    <div class="quality">
      <h3>OUR QUALITY</h3>
      <p>Valmora Productions uses only professional video &amp; audio production equipment. All of our weddings are captured with state-of-the-art HD digital cinema cameras, lenses, and expert filmmaking support gear.</p>
    </div>
    <div class="brand">VALMORA<small>FILMWORKS</small></div>
  </div>
</section>

<section class="page p2">
  <div class="inner">
    <h2 class="heading"><span class="mark"></span>FEATURE FILM PACKAGES:</h2>
    <div class="body">
      <p>Our feature film packages are the signature offering from our studio. These packages are all about storytelling. Our cinematography team will craft a one-of-a-kind film, carefully weaving all of the amazing images and heartfelt sound bytes that we capture at your event. This is wedding cinema at it's finest… a perfect combination of camera, sound, lighting and editing.</p>
      <p class="lead-in">All Feature Film packages include:</p>
      <ul class="dots">
        <li>3 Cinematographers for 10 hours (extra hours as needed can be discussed)</li>
        <li>Film Lighting package at reception (Introductions, First Dances &amp; Toasts)<span class="note">***We will never annoy your guests with on-camera lights; our film style lighting will gracefully enhance your venue and special moments, and beautifully enrich your film and photos. (Not a substitute for DJ Lighting)</span></li>
        <li>Dual system audio for superior sound quality</li>
        <li>Multi camera "Real Time" edits of Ceremony &amp; Reception</li>
        <li>DVD/Blu-Ray or Digital delivery</li>
      </ul>
      <div class="price-box">55 minute total run time w/ 10 minute feature film – 4,995$<br>60 minute total run time w/ 15 minute feature film – 5,595$</div>
      <p>****Total run time depends on length of "real time" edits, which will vary by event.<br>Average run time of these edits is 45 minutes.</p>
    </div>
  </div>
  <div class="grid" style="top:498px;height:272px;grid-template-rows:1fr 1fr">
    <div class="photo" role="img" aria-label="Pink sugar roses on a wedding cake" style="background:linear-gradient(135deg,#f3b8c8,#e57d9c)"></div>
    <div class="photo" role="img" aria-label="Couple dancing under sparkling lights" style="background:linear-gradient(135deg,#cfd9e4,#6f8fb2)"></div>
    <div class="photo" role="img" aria-label="Bride holding a white bouquet" style="background:linear-gradient(135deg,#3a3a3c,#d8d4cf)"></div>
    <div class="photo" role="img" aria-label="Champagne flutes and a bottle" style="background:linear-gradient(135deg,#f4efe2,#c9b887)"></div>
  </div>
</section>

<section class="page p3">
  <div class="inner">
    <h2 class="heading"><span class="mark"></span>CORE PACKAGES:</h2>
    <div class="body">
      <p>Our core packages are designed as the entryway to modern style wedding cinema. Both packages come with a "Featurette" style highlight edit, and supplemented with multi-camera "real time" edits of your wedding day.</p>
      <p class="lead-in">All Core packages include:</p>
      <ul class="dots">
        <li>Dual system audio for pristine quality</li>
        <li>DVD or Blu-Ray (3) with standard cases and artwork</li>
      </ul>
      <div class="label wide">Core Package 1: 2,995$ (in-state only)</div>
      <ul class="ticks">
        <li><svg width="10" height="10" viewBox="0 0 10 10"><rect x=".5" y=".5" width="9" height="9" fill="none" stroke="#1f6fc0"/><path d="M2 5l2 2 4-5" fill="none" stroke="#1f6fc0" stroke-width="1.4"/></svg>2 Cinematographers</li>
        <li><svg width="10" height="10" viewBox="0 0 10 10"><rect x=".5" y=".5" width="9" height="9" fill="none" stroke="#1f6fc0"/><path d="M2 5l2 2 4-5" fill="none" stroke="#1f6fc0" stroke-width="1.4"/></svg>Coverage beginning at ceremony through Cake Cutting (up to 8 hours)</li>
        <li><svg width="10" height="10" viewBox="0 0 10 10"><rect x=".5" y=".5" width="9" height="9" fill="none" stroke="#1f6fc0"/><path d="M2 5l2 2 4-5" fill="none" stroke="#1f6fc0" stroke-width="1.4"/></svg>3-5 minute highlight edit, cut to music</li>
        <li><svg width="10" height="10" viewBox="0 0 10 10"><rect x=".5" y=".5" width="9" height="9" fill="none" stroke="#1f6fc0"/><path d="M2 5l2 2 4-5" fill="none" stroke="#1f6fc0" stroke-width="1.4"/></svg>Ceremony, Reception and Party dancing real time edits</li>
      </ul>
      <div class="label wide">Core Package 2: 3,995$</div>
      <ul class="ticks">
        <li><svg width="10" height="10" viewBox="0 0 10 10"><rect x=".5" y=".5" width="9" height="9" fill="none" stroke="#1f6fc0"/><path d="M2 5l2 2 4-5" fill="none" stroke="#1f6fc0" stroke-width="1.4"/></svg>2 Cinematographers</li>
        <li><svg width="10" height="10" viewBox="0 0 10 10"><rect x=".5" y=".5" width="9" height="9" fill="none" stroke="#1f6fc0"/><path d="M2 5l2 2 4-5" fill="none" stroke="#1f6fc0" stroke-width="1.4"/></svg>Coverage of Preparations through Cake Cutting (up to 10 hours)</li>
        <li><svg width="10" height="10" viewBox="0 0 10 10"><rect x=".5" y=".5" width="9" height="9" fill="none" stroke="#1f6fc0"/><path d="M2 5l2 2 4-5" fill="none" stroke="#1f6fc0" stroke-width="1.4"/></svg>3-5 minute "featurette" edit, cut to music</li>
        <li><svg width="10" height="10" viewBox="0 0 10 10"><rect x=".5" y=".5" width="9" height="9" fill="none" stroke="#1f6fc0"/><path d="M2 5l2 2 4-5" fill="none" stroke="#1f6fc0" stroke-width="1.4"/></svg>Ceremony, Reception and Party dancing real time edits</li>
      </ul>
    </div>
  </div>
  <div class="photo" role="img" aria-label="Couple silhouetted on rocks by the sea at sunset, with wedding rings inset" style="left:0;top:418px;width:509px;height:357px;background:linear-gradient(180deg,#4d5a6e 0%,#d79a5a 38%,#f2c47e 48%,#5b6a78 62%,#1f2326 100%)"></div>
</section>

<section class="page p4">
  <div class="inner">
    <h2 class="heading"><span class="mark"></span>ADDITIONAL OPTIONS:</h2>
    <div class="body">
      <div class="label slim">Instant Teaser – 200$</div>
      <p>Our feature film packages are the signature offering from our studio. These packages are all about storytelling. Our cinematography team will craft a one-of-a-kind film, carefully weaving all of the amazing images and heartfelt sound bytes that we capture at your event. This is wedding cinema at it's finest… a perfect combination of camera, sound, lighting and editing.</p>
      <div class="label slim">Same Day-Edit – 1,800$</div>
      <p>We will create a 3-5 minute film ready to show no earlier than cake cutting, no later than end of reception. We do not provide display, must be provided by venue/DJ.<br>***Available on packages with Bride &amp; Groom Preparations only.</p>
      <div class="label slim">Save-the-Date Film – Contact for Custom Quote</div>
      <p>We will create a 30-60 second film, letting you tell your short love story, and announce your engagement to the world.</p>
      <div class="label slim">Rehearsal Party coverage – 900$</div>
      <p>Two of our cinematographers will be there to capture some of the special moments from your rehearsal dinner, and intertwine some of the images and sound with your feature film. This option is ideal only when there will be special speeches during the party.</p>
      <div class="label slim" style="line-height:1.4">Custom Designed Premium Discs &amp; Case – 115$ each<br>Digital Copies on Custom USB Drive – 95$</div>
    </div>
  </div>
  <div class="grid" style="top:452px;height:318px;grid-template-rows:1fr 1fr">
    <div class="photo" role="img" aria-label="Candlelit table with bride and groom chair signs" style="background:linear-gradient(135deg,#2d2a26,#b79b72)"></div>
    <div class="photo" role="img" aria-label="Black and white photo of the couple kissing" style="background:linear-gradient(135deg,#1e1e1e,#9a9a9a)"></div>
    <div class="photo" role="img" aria-label="Guests dancing at a reception under purple light" style="background:linear-gradient(135deg,#2c1f5c,#8e4fc4)"></div>
    <div class="photo" role="img" aria-label="Venue building lit at night under a blue sky" style="background:linear-gradient(180deg,#0f2c6b,#3a68b8)"></div>
  </div>
</section>

<section class="page p5">
  <div class="inner faq">
    <h2 class="heading"><span class="mark"></span>FREQUENTLY ASKED QUESTIONS</h2>
    <h4>Are you guys invisible on my wedding day?</h4>
    <p>No, we aren't, but we constantly receive funny comments from our clients. They sometimes wonder if we even made it to the reception. It's our goal to always be shooting candidly, and unobtrusively as possible. With three camera's, we can sit from afar and capture intimate moments with out running around your ceremony to get a terrific shot.</p>
    <h4>How does your booking process work?</h4>
    <p>All event bookings are first come, first served. Once we receive a request to book from our client, we place a temporary 7 day hold on your date pending receipt of a 25% retainer and completed contract, which is done through our online booking system. Final payment is due 21 days prior to the event.</p>
    <h4>How long does it take to receive our film?</h4>
    <p>Our contract gives us 6 months to complete your film, though we generally deliver much quicker than that, according to the length of the edit. We reserve this amount of time as a safeguard.</p>
    <h4>Do you offer raw footage?</h4>
    <p>We don't shoot for coverage, but instead shoot subjectively with the goal of creating a modern wedding film, instead of a traditional coverage video. We will capture the entire ceremony and all key events at the reception, so we don't think that it's something worth your investment. Still, if you must have it, we charge 750$ and client must provide a 1tb hard drive for the transfer.</p>
    <h4>What type of equipment do you use?</h4>
    <p>Super 35mm cinema cameras and lenses. (They are small). Once in awhile we will whip out a DSLR for our B camera. We own tons of professional support gear as well, to help us create awesome production value for your film.</p>
    <h4>I love the way you weave sounds throughout your films,<br>how do you get such great audio?</h4>
    <p>We take audio very seriously, it's half of the film. We'll put small Lavalier mics on the groom and officiant, hide a recorder at the podium, and tap in to your DJ's mix board. In the film world, this is called dual-system audio.</p>
    <h4>We are getting married outside the NY/Philly metro area, in fact, it<br>may be a destination wedding, how much to get you guys to come?</h4>
    <p>Outside the NYC or Philadelphia metro areas is generally on a case by case basis, but usually we require 2-3 nights lodging for our crew, as well as flight costs if necessary.</p>
    <h4>Who picks the music for my film?</h4>
    <p>We ask that you give us complete creative control over editing, which includes song selections. This allows us to use our talents to create something great. We will use licensed music so that there are no copyright infringements, and so that you won't have your film pulled down off of the Internet.</p>
    <h4>Are you insured?</h4>
    <p>Yes, we carry a full liability insurance policy, and we are a registered business.</p>
  </div>
</section>

<section class="page p6">
  <div class="top"></div>
  <div class="venues">
    <div class="photo" role="img" aria-label="Ornate white venue facade under a blue sky" style="background:linear-gradient(180deg,#8fb3d9,#e9ecef 60%,#6f7d5a)"></div>
    <div class="photo" role="img" aria-label="Mansion venue with lawn and trees" style="background:linear-gradient(180deg,#9cc0e0,#f1f1ee 55%,#4f6b38)"></div>
  </div>
  <div class="band"></div>
  <div class="about">
    <h2>ABOUT US</h2>
    <p>Receiving professional recognition throughout the industry, Valmora Filmworks has intertwined true filmmaking techniques with the individual stories they encounter to create compelling and visually polished films.</p>
    <p>Harnessing a background in narrative filmmaking, these films are produced with the tried and true methods of visual storytelling that have been used by filmmakers in cinema since the advent of motion pictures. Utilizing real digital cinema cameras and support gear, we are able to deliver visually stunning images that will be carefully crafted in to a wedding film that fits you just right.</p>
    <p>We pay attention to the little details. The tear in a guests eye during your vows. The best man preparing his speech. Your favorite dog in his own custom tux. All of these little moments add up to the creation of your story, your wedding film, that will be cherished for a lifetime.</p>
    <p>We know how much work is involved in planning the perfect day. So give us a call or fill out our contact form today, and we'll take care of the rest.</p>
    <p class="loc">Our Location: Valmora Productions is located out of central New Jersey, but is available as your cinematographer anywhere. We are available to travel out of state, and also to destination weddings, our US passport is always current.</p>
  </div>
  <div class="bottom">
    <div class="award">AWARD WINNING CINEMATOGRAPHY</div>
    <div class="badges">
      <svg width="92" height="92" viewBox="0 0 92 92" role="img" aria-label="Award badge"><circle cx="46" cy="46" r="40" fill="none" stroke="#fff" stroke-width="2"/></svg>
      <svg width="92" height="92" viewBox="0 0 92 92" role="img" aria-label="Award badge"><circle cx="46" cy="46" r="40" fill="none" stroke="#fff" stroke-width="2"/></svg>
    </div>
    <div class="brand">VALMORA<small>FILMWORKS</small></div>
    <ul class="contact">
      <li><svg width="10" height="12" viewBox="0 0 10 12"><path d="M5 0a4 4 0 0 0-4 4c0 3 4 8 4 8s4-5 4-8a4 4 0 0 0-4-4z" fill="#fff"/><circle cx="5" cy="4" r="1.5" fill="#1c1c1e"/></svg>48 Alder Lane, Westfield, NJ 07090</li>
      <li class="phone"><svg width="11" height="11" viewBox="0 0 11 11"><circle cx="5.5" cy="5.5" r="5" fill="none" stroke="#fff"/><path d="M3.5 3c.6 2.3 2 3.8 4 4.5l.6-1-1-.6" fill="none" stroke="#fff" stroke-width="1.2"/></svg>732.555.0148</li>
      <li><svg width="11" height="11" viewBox="0 0 11 11"><circle cx="5.5" cy="5.5" r="4.8" fill="none" stroke="#fff"/><ellipse cx="5.5" cy="5.5" rx="2" ry="4.8" fill="none" stroke="#fff"/><path d="M.7 5.5h9.6" stroke="#fff"/></svg>www.valmorafilmworks.com</li>
    </ul>
  </div>
  <div class="band2"></div>
</section>

</body>
</html>
```